Bref créative
see logo info from logo info
Bluefern Trading Partners, Ltd.
Use same font as used in my logo
can also give other font suggestions
Modern
Daniel Okafor
President
742 Hollis St. - Suite 0830
New York, NY 10093
212-555-0147 Ext-305
sales@bluefernexample.com
bluefernexample.com
we are looking for business card and stationary design layouts.
logo with name
This is our logo to be used for the layout of the business cards and stationary.

```html
<!DOCTYPE html>
<html lang="en">
<head>
<meta charset="utf-8">
<title>Bluefern Trading Partners, Ltd. — Stationery Concepts</title>
<link rel="stylesheet" href="https://fonts.googleapis.com/css2?family=Open+Sans:wght@400;600;700&display=swap">
<style>
  :root {
    --blue: #1f50b8;
    --navy: #1d2a47;
    --paper: #ffffff;
    --ink: #3a4357;
    --muted: #8a93a6;
    --backdrop: #e8e6e2;
    --label: #6b6b6b;
  }
  * { box-sizing: border-box; margin: 0; padding: 0; }
  html, body { width: 1200px; height: 466px; overflow: hidden; }
  body {
    background: var(--backdrop);
    font-family: "Open Sans", Arial, sans-serif;
    color: var(--ink);
    position: relative;
  }
  .piece { position: absolute; background: var(--paper); overflow: hidden; box-shadow: 0 2px 6px rgba(0,0,0,.18); }
  .piece svg.shape { position: absolute; inset: 0; width: 100%; height: 100%; }
  .caption {
    position: absolute; font-size: 7px; letter-spacing: 1px;
    text-transform: uppercase; color: var(--label); font-weight: 600;
  }
  .brand {
    position: absolute; display: flex; align-items: center; gap: 4px;
    font-weight: 700; color: var(--navy); text-transform: uppercase; white-space: nowrap;
  }
  .brand .dot { border-radius: 50%; background: var(--blue); flex: none; }
  .brand.light { color: #fff; }
  .brand.light .dot { background: #fff; }
  .contact { position: absolute; font-size: 4.6px; line-height: 7px; color: var(--ink); }
  .contact .name { font-weight: 700; font-size: 6px; color: var(--navy); }

  /* business cards */
  .card { width: 124px; height: 72px; left: 12px; }
  .card-front { top: 170px; }
  .card-back { top: 268px; background: var(--blue); }

  /* letterheads */
  .letterhead { width: 264px; height: 404px; top: 22px; }
  .letterhead-one { left: 182px; }
  .letterhead-two { left: 466px; }
  .footer-line {
    position: absolute; font-size: 5px; color: #fff; white-space: nowrap;
    display: flex; gap: 10px;
  }

  /* envelopes */
  .envelope { width: 330px; height: 88px; left: 848px; }
  .env-1 { top: 20px; }
  .env-2 { top: 116px; background: var(--navy); }
  .env-3 { top: 212px; }
  .env-4 { top: 318px; left: 820px; width: 340px; height: 108px; }
</style>
</head>
<body>

  <p class="caption" style="left:12px;top:156px;">Stationery Concepts</p>

  <!-- Business card front -->
  <div class="piece card card-front">
    <svg class="shape" viewBox="0 0 124 72" preserveAspectRatio="none" aria-hidden="true">
      <path d="M0 48 C30 56 60 66 86 72 L0 72 Z" fill="var(--blue)"/>
      <path d="M0 54 C26 60 50 68 66 72 L0 72 Z" fill="var(--navy)"/>
    </svg>
    <div class="brand" style="left:8px;top:9px;font-size:4.4px;">
      <span class="dot" style="width:7px;height:7px;"></span>Bluefern Trading Partners, Ltd.
    </div>
    <div class="contact" style="left:64px;top:26px;">
      <div class="name">Daniel Okafor</div>
      <div>President</div>
      <div>742 Hollis St. - Suite 0830</div>
      <div>New York, NY 10093</div>
      <div>212-555-0147 Ext-305</div>
      <div>sales@bluefernexample.com</div>
    </div>
  </div>
  <p class="caption" style="left:12px;top:248px;">Business Card Front</p>

  <!-- Business card back -->
  <div class="piece card card-back">
    <svg class="shape" viewBox="0 0 124 72" preserveAspectRatio="none" aria-hidden="true">
      <path d="M0 60 C40 66 80 70 124 62 L124 72 L0 72 Z" fill="var(--navy)"/>
    </svg>
    <div class="brand light" style="left:20px;top:31px;font-size:4.4px;">
      <span class="dot" style="width:7px;height:7px;"></span>Bluefern Trading Partners, Ltd.
    </div>
  </div>
  <p class="caption" style="left:12px;top:346px;">Business Card Back</p>

  <!-- Letterhead option 1 -->
  <div class="piece letterhead letterhead-one">
    <svg class="shape" viewBox="0 0 264 404" preserveAspectRatio="none" aria-hidden="true">
      <path d="M230 0 L264 0 L264 404 L250 404 C262 280 262 120 230 0 Z" fill="var(--blue)"/>
      <path d="M214 0 L232 0 C258 110 262 270 252 404 L244 404 C252 260 246 110 214 0 Z" fill="var(--navy)"/>
    </svg>
    <div class="brand" style="left:72px;top:22px;font-size:5.4px;">
      <span class="dot" style="width:9px;height:9px;"></span>Bluefern Trading Partners, Ltd.
    </div>
    <div class="contact" style="left:22px;top:356px;">
      <div>742 Hollis St. - Suite 0830</div>
      <div>New York, NY 10093</div>
      <div>212-555-0147 Ext-305</div>
      <div>bluefernexample.com</div>
    </div>
  </div>
  <p class="caption" style="left:270px;top:436px;">Letter Head Option 1</p>

  <!-- Letterhead option 2 -->
  <div class="piece letterhead letterhead-two">
    <svg class="shape" viewBox="0 0 264 404" preserveAspectRatio="none" aria-hidden="true">
      <path d="M0 330 C70 388 180 396 264 340 L264 404 L0 404 Z" fill="var(--navy)"/>
      <path d="M0 352 C80 396 190 400 264 358 L264 404 L0 404 Z" fill="var(--blue)"/>
    </svg>
    <div class="brand" style="left:72px;top:22px;font-size:5.4px;">
      <span class="dot" style="width:9px;height:9px;"></span>Bluefern Trading Partners, Ltd.
    </div>
    <div class="footer-line" style="left:28px;top:388px;">
      <span>742 Hollis St. - Suite 0830, New York, NY 10093</span>
      <span>212-555-0147</span>
      <span>bluefernexample.com</span>
    </div>
  </div>
  <p class="caption" style="left:554px;top:436px;">Letter Head Option 2</p>

  <!-- Envelopes -->
  <div class="piece envelope env-1">
    <svg class="shape" viewBox="0 0 330 88" preserveAspectRatio="none" aria-hidden="true">
      <path d="M300 0 L330 0 L330 88 L318 88 C330 60 326 24 300 0 Z" fill="var(--blue)"/>
      <path d="M290 0 L302 0 C326 24 330 60 316 88 L310 88 C322 58 318 26 290 0 Z" fill="var(--navy)"/>
    </svg>
    <div class="brand" style="left:14px;top:12px;font-size:4.4px;">
      <span class="dot" style="width:7px;height:7px;"></span>Bluefern Trading Partners, Ltd.
    </div>
  </div>

  <div class="piece envelope env-2">
    <svg class="shape" viewBox="0 0 330 88" preserveAspectRatio="none" aria-hidden="true">
      <path d="M0 0 L165 44 L330 0" fill="none" stroke="#2c3a5c" stroke-width="1"/>
    </svg>
    <div class="brand light" style="left:130px;top:60px;font-size:4.4px;">
      <span class="dot" style="width:7px;height:7px;"></span>Bluefern Trading Partners, Ltd.
    </div>
  </div>

  <div class="piece envelope env-3">
    <svg class="shape" viewBox="0 0 330 88" preserveAspectRatio="none" aria-hidden="true">
      <path d="M0 0 L165 40 L330 0" fill="none" stroke="#dde1e8" stroke-width="1"/>
    </svg>
    <div class="brand" style="left:130px;top:58px;font-size:4.4px;">
      <span class="dot" style="width:7px;height:7px;"></span>Bluefern Trading Partners, Ltd.
    </div>
  </div>

  <div class="piece envelope env-4">
    <svg class="shape" viewBox="0 0 340 108" preserveAspectRatio="none" aria-hidden="true">
      <path d="M318 0 L340 0 L340 108 L318 108 Z" fill="var(--blue)"/>
      <path d="M308 0 L316 0 L316 108 L308 108 Z" fill="var(--navy)"/>
    </svg>
    <div class="brand" style="left:14px;top:14px;font-size:4.4px;">
      <span class="dot" style="width:7px;height:7px;"></span>Bluefern Trading Partners, Ltd.
    </div>
  </div>

  <p class="caption" style="left:1040px;top:432px;">Envelope Options</p>

</body>
</html>
```